Bottle label design for a mulberry brandy

Please create a label design for a mulberry brandy. The registered brand name is "Kolvat"
The brandy will be produced in Armenia from 100% mulberry.
Color of the product: transparent.
The product will be sold worldwide. The price will be between 30 and 50 USD. So the product will be in premium category.
Therefore we need a solid design, appropriate to the product price category. The design, however, needs to be modern and optimistic.
You can have mulberries on the label or not have, it is up to you.
We have chosen for the product some bottle types, the links to the available bottles you can find in the attachment. Ideally you show a picture of your label on the bottle you selected.

Target Market(s)

worldwide

```html
<!DOCTYPE html>
<html lang="en">
<head>
<meta charset="utf-8">
<title>Kolvat Mulberry Brandy Labels</title>
<link href="https://fonts.googleapis.com/css2?family=Cinzel:wght@400;500&family=Raleway:wght@400&display=swap" rel="stylesheet">
<style>
  :root {
    --paper: #ffffff;
    --plum: #5a0322;
    --gold: #e8a40c;
    --ink: #3a0510;
    --art-gold: #b8720f;
    --art-ink: #e9dfe1;
  }
  html, body {
    margin: 0;
    padding: 0;
    width: 800px;
    height: 1200px;
    overflow: hidden;
    background: var(--paper);
  }
  .canvas {
    width: 800px;
    height: 1200px;
    display: flex;
    flex-direction: column;
    align-items: center;
    justify-content: space-between;
    padding: 90px 0;
    box-sizing: border-box;
  }
  .label { display: block; }
  .label-plum { width: 320px; height: 452px; }
  .label-ivory { width: 272px; height: 468px; }
  .brand-name {
    font-family: "Cinzel", serif;
    font-weight: 500;
    text-anchor: middle;
  }
  .label-info {
    font-family: "Raleway", sans-serif;
    font-weight: 400;
    text-anchor: middle;
    letter-spacing: 0.2px;
  }
  .label-plum .brand-name, .label-plum .label-info { fill: var(--gold); }
  .label-ivory .brand-name, .label-ivory .label-info { fill: var(--ink); }
</style>
</head>
<body>
<main class="canvas">

  <svg class="label label-plum" viewBox="75 120 400 565" aria-label="Kolvat label, plum version">
    <path class="label-shape" fill="var(--plum)"
      d="M80,640 L135,200 Q140,128 275,128 Q410,128 415,200 L470,640 Q472,680 430,680 L120,680 Q78,680 80,640 Z"/>
    <path class="label-border" fill="none" stroke="var(--gold)" stroke-width="2"
      d="M108,630 L152,205 Q160,155 275,155 Q390,155 400,205 L445,630 Q445,655 420,655 L130,655 Q105,655 108,630 Z"/>
    <rect class="label-art" role="img" aria-label="Line illustration of a mulberry branch with two berries and two leaves"
      x="180" y="175" width="196" height="135" rx="20" fill="var(--art-gold)" opacity="0.35"/>
    <g class="name-band" stroke="var(--gold)" stroke-width="2">
      <line x1="140" y1="362" x2="410" y2="362"/>
      <line x1="132" y1="436" x2="418" y2="436"/>
    </g>
    <text class="brand-name" x="275" y="417" font-size="56">KOLVAT</text>
    <text class="label-info" x="275" y="527" font-size="13">100% MULBERRY</text>
    <text class="label-info" x="275" y="587" font-size="13">70 CL / 23.67 OZ</text>
    <text class="label-info" x="275" y="636" font-size="13">PRODUCED IN ARMENIA</text>
  </svg>

  <svg class="label label-ivory" viewBox="95 830 340 585" aria-label="Kolvat label, ivory version">
    <path class="label-frame" fill="var(--paper)" stroke="var(--ink)" stroke-width="3"
      d="M100,1390 L100,930 L120,930 L120,915 L138,915 L138,880 Q138,835 264,835 Q390,835 390,880 L390,915 L410,915 L410,930 L430,930 L430,1390 L410,1390 L410,1410 L120,1410 L120,1390 Z"/>
    <path class="label-frame-inner" fill="none" stroke="var(--ink)" stroke-width="1.2"
      d="M108,1382 L108,938 L128,938 L128,923 L146,923 L146,882 Q146,843 264,843 Q382,843 382,882 L382,923 L402,923 L402,938 L422,938 L422,1382 L402,1382 L402,1402 L128,1402 L128,1382 Z"/>
    <rect class="label-art" role="img" aria-label="Line illustration of a mulberry branch with two berries and two leaves"
      x="160" y="880" width="210" height="175" rx="20" fill="var(--art-ink)"/>
    <g class="name-band" stroke="var(--ink)" stroke-width="1.5">
      <line x1="112" y1="1100" x2="418" y2="1100"/>
      <line x1="112" y1="1180" x2="418" y2="1180"/>
    </g>
    <text class="brand-name" x="265" y="1162" font-size="62">KOLVAT</text>
    <text class="label-info" x="260" y="1254" font-size="15">100% MULBERRY</text>
    <text class="label-info" x="256" y="1322" font-size="15">70 CL / 23.67 OZ</text>
    <text class="label-info" x="261" y="1376" font-size="15">PRODUCED IN ARMENIA</text>
  </svg>

</main>
</body>
</html>
```